Creative BLOG HEADER and NEWSLETTER OPTIN for a Training Consultant

What I do
I am a training consultant, mentor and coach specialised in training trainers to train more effectively by showing them how to hack the way people learn. I also help training consultant to commercialise their intellectual property and work with entrepreneurs, small business owners and professionals changing careers who need to gain clarity and apply strategic thinking to their next steps.
See more on http://tobiasfernlund.com.au/about-tobias/ .
My background is in Business, Marketing, Innovation capability and Learning & Development.
Communicate differentiation:
I have a minimalist blog that I am happy with, but I need a HEADER and an OPT-IN FORM designed to help me communicate my unique selling proposition and differentiate myself from old-school training consultants.
The programs I offer are different because they are outcome or result driven with emphasis on applied creativity and problem solving. While traditional training consultants focus on knowledge transfer, I focus on facilitating tangible outcomes.
I focus a lot on "Unpacking my clients brains" before offering advice. When I start to work with a new client, be it a coaching or training client, I use a A5 blank sheet as a canvas to make the process of "unpacking the client's brain" more visual and clearly define the desired outcomes.
I rely strongly in strategy and a hacker's mindset to generate outcomes from client.
Header requirement:
- I'd like my blog to communicate my process of debriefing new clients ("unpacking brains")
- I'd like the design to have a 'sketchy' feel
- I'd like a design that communicates playfulness, applied creativity, a hackers mindset, strategy, results orientation and street smart learning.
- Social Media ICONS and contact info on top
Visual references:
See a banner I had designed attached. It would be nice to follow the same kind of concept.
Other visual references:
http://imagecrate.example/item/3d-metal-human-brain-inside-pencil-light-bulb-with-business-stra/4815206
http://imagecrate.example/item/hannd-drawing-light-bulb-and-creative-word-design-as-concept/3927154
Optin form:
- A newsletter opt-in form to be uploaded on the sidebar (i use postwren) with headline: "Shifting Tides Monthly Newsletter" and a call to action.
I do want to use my photo, but not sure how to go about that. Accepting suggestions.
Best photo I have attached.
See reference for USER EXPERIENCE http://clearpanel.example/
Updates
Project Deadline Extended
Reason: Received one great design that didn't fully fit the briefing. Trying to collaborate with designer to solve the issue.
Still accepting entries though.
Cheers,
Tobais
- Helvetica

```html
<!DOCTYPE html>
<html lang="en">
<head>
<meta charset="utf-8">
<title>Kindlewell Training and Development</title>
<link rel="stylesheet" href="https://fonts.googleapis.com/css2?family=Oswald:wght@300;400;500&family=Lato:wght@400;700;900&display=swap">
<style>
:root{
  --blue:#1c4f8f;
  --blue-dark:#0d3a73;
  --nav-top:#1f5ea8;
  --nav-bottom:#0b3d7c;
  --green-top:#72ac4a;
  --green-bottom:#3f8a2a;
  --text:#3a3a3a;
  --muted:#555;
  --paper:#ececec;
  --footer:#333;
  --white:#fff;
}
*{box-sizing:border-box;margin:0;padding:0}
html,body{width:1200px;height:1179px;overflow:hidden}
body{font-family:"Lato",sans-serif;color:var(--text);background:var(--white);position:relative}
.wrap{position:absolute;left:172px;width:856px}

/* header */
.site-header{position:absolute;top:0;left:0;width:1200px;height:122px;background:linear-gradient(#f1f1f1,#e6e6e6)}
.brand{top:26px;display:flex;align-items:center;gap:10px}
.brand-mark{width:22px;height:22px;border-radius:50%;background:var(--blue)}
.brand-name{font-family:"Lato",sans-serif;font-weight:900;font-size:50px;color:var(--blue);letter-spacing:1px;line-height:1}
.social{position:absolute;right:172px;top:9px;display:flex;gap:6px}
.social span{width:27px;height:27px;border-radius:50%;display:block}
.social .s1{background:#3b5a9a}.social .s2{background:#29a9e1}.social .s3{background:#1176b4}.social .s4{background:#f08a24}
.enquiry{position:absolute;right:172px;top:54px;width:198px;height:49px;border:1px solid #c8c8c8;background:linear-gradient(#fdfdfd,#ebebeb);display:flex;align-items:center;padding-left:8px;gap:6px}
.enquiry small{display:block;font-size:15px;color:#444}
.enquiry strong{display:block;font-family:"Oswald",sans-serif;font-weight:500;font-size:21px;color:var(--blue);line-height:1.05}

/* nav */
.main-nav{position:absolute;top:122px;left:0;width:1200px;height:49px;background:linear-gradient(var(--nav-top),var(--nav-bottom));border-top:2px solid #3f7fc6}
.main-nav ul{list-style:none;display:flex;position:absolute;left:172px;top:0;height:47px}
.main-nav li{font-family:"Oswald",sans-serif;font-size:19px;color:var(--white);display:flex;align-items:center;justify-content:center;height:47px;border-right:1px solid #0a3268;text-transform:uppercase}
.main-nav li.active{background:linear-gradient(var(--green-top),var(--green-bottom))}

/* hero */
.hero{position:absolute;top:171px;left:0;width:1200px;height:468px;background:linear-gradient(90deg,#8a8a8a,#7a7a7a 45%,#9a9a9a)}
.hero-art{position:absolute;left:560px;top:0;width:640px;height:468px;background:radial-gradient(circle at 20% 30%,#d6d6d6,#a9a9a9 45%,#8e8e8e 100%)}
.hero-copy{top:50px}
.hero h1{font-family:"Oswald",sans-serif;font-weight:400;font-size:39px;color:var(--white);line-height:1.1;letter-spacing:-.5px}
.hero .lead{font-family:"Oswald",sans-serif;font-weight:300;font-size:22px;color:var(--white);line-height:30px;margin-top:12px;width:400px}
.ticks{list-style:none;margin-top:18px}
.ticks li{display:flex;align-items:center;gap:10px;font-size:20px;font-weight:700;color:var(--white);height:37.5px}
.btn-more{margin-top:32px;width:178px;height:48px;border-radius:4px;background:linear-gradient(#f4f4f4,#c9c9c9);box-shadow:0 10px 12px -6px rgba(0,0,0,.45);display:flex;align-items:center;justify-content:space-between;padding:0 14px 0 15px;font-size:26px;font-weight:700;color:var(--blue-dark)}

/* about */
.about{position:absolute;top:639px;left:0;width:1200px;height:339px;background:linear-gradient(#f2f2f2,#fff 25%)}
.section-title{font-family:"Oswald",sans-serif;font-weight:400;font-size:35px;color:#333;display:flex;align-items:center;gap:10px}
.section-title em{font-style:normal;color:var(--blue)}
.section-title .rule{flex:1;height:1px;background:#c9c9c9;margin-left:4px;position:relative}
.section-title .rule::before{content:"";position:absolute;left:-12px;top:-4px;width:8px;height:8px;border:1px solid #c9c9c9}
.about-title{top:30px}
.about-body{top:82px;width:620px;font-size:14.3px;line-height:22.5px;color:#444}
.about-body p+p{margin-top:9px}
.portrait{position:absolute;left:835px;top:75px;width:186px;height:187px;background:linear-gradient(135deg,#b3a16e,#6e6a3a 55%,#2c2c28)}
.portrait-name{position:absolute;left:835px;top:268px;width:200px;text-align:center;font-family:"Oswald",sans-serif;font-size:21px;color:var(--blue)}

/* newsletter */
.newsletter{position:absolute;top:978px;left:0;width:1200px;height:150px;background:linear-gradient(#e7e7e7,#f3f3f3)}
.nl-title{position:absolute;top:12px;left:0;width:1200px;display:flex;justify-content:center;align-items:center;gap:14px;font-family:"Oswald",sans-serif;font-size:33px;color:#3a3a3a}
.nl-title em{font-style:normal;color:var(--blue)}
.nl-text{position:absolute;top:74px;width:1200px;text-align:center;font-size:15px;color:#444}
.field{position:absolute;top:100px;width:270px;height:29px;border:1px solid #cfcfcf;background:var(--white);font-size:12.5px;color:#666;display:flex;align-items:center;justify-content:space-between;padding:0 8px}
.btn-signup{position:absolute;left:806px;top:100px;width:158px;height:30px;background:linear-gradient(#1d5aa2,#0c3c78);border-bottom:3px solid #072a57;color:var(--white);font-size:17.5px;font-weight:700;text-align:center;line-height:28px}

/* footer */
.site-footer{position:absolute;top:1128px;left:0;width:1200px;height:51px;background:var(--footer);color:var(--white);font-size:12.5px}
.foot-links{position:absolute;left:173px;top:18px;display:flex;align-items:center}
.foot-links .sep{margin:0 22px;color:#aaa;font-weight:700;letter-spacing:-1px}
.copyright{position:absolute;right:173px;top:18px}
</style>
</head>
<body>

<header class="site-header">
  <div class="wrap brand">
    <span class="brand-mark"></span>
    <span class="brand-name">KINDLEWELL</span>
  </div>
  <div class="social" aria-label="Social links">
    <span class="s1"></span><span class="s2"></span><span class="s3"></span><span class="s4"></span>
  </div>
  <div class="enquiry">
    <svg width="36" height="42" viewBox="0 0 36 42" aria-hidden="true">
      <path d="M6 4c3-3 7-3 8 1l2 7c1 3-2 4-3 5 1 4 4 8 8 11 1-1 3-3 5-2l6 4c3 2 2 6-1 8-6 5-18-2-24-13S2 8 6 4z" fill="#1c4f8f"/>
    </svg>
    <div><small>Call for Enquiry</small><strong>(61) 400 555 019</strong></div>
  </div>
</header>

<nav class="main-nav">
  <ul>
    <li class="active" style="width:126px">Home</li>
    <li style="width:138px">Blog</li>
    <li style="width:248px">About the Author</li>
    <li style="width:214px">Work with me</li>
    <li style="width:130px;border-right:0">Contact</li>
  </ul>
</nav>

<section class="hero">
  <div class="hero-art" role="img" aria-label="Pencil light bulb with a brain inside, surrounded by sketched bulbs and words such as ideas, mentor, strategy and goal"></div>
  <div class="wrap hero-copy">
    <h1>I AM A TRAINING CONSULTANT,</h1>
    <p class="lead">Mentor and coach specialized in training trainers to train more effectively by showing them how to hack the way people learn.</p>
    <ul class="ticks">
      <li><svg width="16" height="16" viewBox="0 0 16 16"><rect width="16" height="16" rx="3" fill="#fff"/><path d="M4 8l3 3 5-6" stroke="#7d7d7d" stroke-width="2.2" fill="none"/></svg>Lorem ipsum dolor sit amet construct</li>
      <li><svg width="16" height="16" viewBox="0 0 16 16"><rect width="16" height="16" rx="3" fill="#fff"/><path d="M4 8l3 3 5-6" stroke="#7d7d7d" stroke-width="2.2" fill="none"/></svg>Vestibulum tempor metus arcu into amet</li>
      <li><svg width="16" height="16" viewBox="0 0 16 16"><rect width="16" height="16" rx="3" fill="#fff"/><path d="M4 8l3 3 5-6" stroke="#7d7d7d" stroke-width="2.2" fill="none"/></svg>Nunc euismod, nisl eget dapibus</li>
    </ul>
    <div class="btn-more">View More <svg width="10" height="14" viewBox="0 0 10 14"><path d="M0 0l10 7-10 7z" fill="#888"/></svg></div>
  </div>
</section>

<section class="about">
  <h2 class="wrap section-title about-title">About <em>Tobias Fernlund</em><span class="rule"></span></h2>
  <div class="wrap about-body">
    <p>I am a self confessed learning and development freak. A hacker of all things related to optimised learning capacity and things that put us into a state of flow. I’ve been a lifetime students of what makes us tick and I always had an insatiable curiosity for uncovering strategies to make real change happen.</p>
    <p>Lorem ipsum dolor sit amet, consectetuer adipiscing elit, sed diam nonua nibh euismod tincidunt ut laoreet dolore magna aliquam erat volutpat. in Ut wisi enim ad minim veniam, quis nostrud exerci in tation ullamcorpe a suscipit lobortis nisl ut aliquip ex ea commodo consequat. Duis autemipk velipas eum iriure dolor in hendrerit in vulputate velit esse molestie consequ, vel illum dolore eu feugiat.</p>
  </div>
  <div class="portrait" role="img" aria-label="Portrait photo of Tobias Fernlund outdoors among tree roots"></div>
  <div class="portrait-name">Tobias Fernlund</div>
</section>

<section class="newsletter">
  <h2 class="nl-title">
    <svg width="36" height="36" viewBox="0 0 36 36" aria-hidden="true"><path d="M2 16L18 3l16 13v18H2z" fill="#6b6b6b"/><path d="M2 16l16 11 16-11" stroke="#e9e9e9" stroke-width="2" fill="none"/><path d="M18 8v10M13 14l5 5 5-5" stroke="#e9e9e9" stroke-width="3" fill="none"/></svg>
    <span>Kindlewell Training <em>Monthly Newsletter</em></span>
  </h2>
  <p class="nl-text">Leave your email address to receive our monthly newsletter containing the latest news and informationine .</p>
  <div class="field" style="left:217px">Your Name
    <svg width="18" height="18" viewBox="0 0 18 18"><circle cx="9" cy="5" r="4" fill="#bbb"/><path d="M1 18c0-6 4-8 8-8s8 2 8 8z" fill="#bbb"/></svg></div>
  <div class="field" style="left:516px">Your Email
    <svg width="18" height="13" viewBox="0 0 18 13"><rect x=".5" y=".5" width="17" height="12" fill="none" stroke="#aaa"/><path d="M1 1l8 6 8-6" stroke="#aaa" fill="none"/></svg></div>
  <div class="btn-signup">SIGN UP NOW</div>
</section>

<footer class="site-footer">
  <div class="foot-links">
    <span>Home</span><span class="sep">::</span>
    <span>Blog</span><span class="sep">::</span>
    <span>About The Author</span><span class="sep">::</span>
    <span>Work With Me</span><span class="sep">::</span>
    <span>Contact</span>
  </div>
  <div class="copyright">© 2014 Tobias Fernlund.&nbsp; ALL RIGHTS RESERVED.</div>
</footer>

</body>
</html>
```